LIFE CHANGING NEW WEBSITE DESIGN NEEDED FOR FULL WEBSITE- FUN/FEMININE!

I need a website designed for a personal financial advice website geared at women called LADY COIN MAVEN. I will be providing free financial advice around topics of making, saving, spending and sharing money. The concept is to change the way women understand money and the necessity around building various passive income streams to ensure full financial freedom. This will then carry down to advice for mothers with children and children in particular. The website should be elegant and yet witty. I don't want lots of serious photos but more relatable. I will have a photo of myself and my story as this is a blog and needs to be relatable to women and mothers. I like pinks and greys. I want to have a pink piggy bank being broken with a hammer in the front screen to break our traditional mindset around piggy bank saving/spending habits. I have created a logo that is a pink piggy head with LADY COIN MAVEN that needs to be incorporated so that it blends into the heading. I have also already started designing the website on Squarespace and can provide access to that. Basically it should have a format of LADY COIN MAVEN LOGO center in header then on left hand navigation: MAKE, SAVE, SPEND, SHARE then on right hand header navigation: MISSION, GET STARTED, CONTACT LCM I would like to have the front page when you go to the url to have the image of the piggy bank being broken then a catchy phrase then under 4 boxes with MAKE (image and description) SAVE (image and description) SPEND (image and description) SHARE (image and description) if you click on those or the title they go to pages that are dedicated to each them. Each page should have a little intro on the topic then I want lots of blog links as I will be mainly writing blogs. Each blog site should have ability to write comments as well. I need social media icons on each page too. Please let me know what you need from me to get started. I prefer having a discussion if possible to not waste anyone's time. I need the site to be easy for me to use and add blogs/urls etc as needed. I also need the site to be put into my domain that I already purchased: www.ladycoinmaven.example

Target Market(s)

teenage girls, 20 something girls, 30 something girls and mothers

Coding

Coded - Design and coding required

Number of Pages Required

5+ page

Font styles to use
Sans Serif

Colors
e667a6
e34197
f59195
eea4c8
aaaaaa
cbcbcb
959595

Requirements
Must have
• TOP NAVIGATION
• MAKE SAVE SPEND SHARE LOGO/LADY COIN MAVEN MISSION GET STARTED CONTACT LCM
• FRONT PAGE: IMAGE OF PIGGY BANK BEING BROKEN WITH A HAMMER
• CATCH PHRASE OVER THE IMAGE
• BUTTON IN PINK- TAKE ACTION (WHICH DIRECTS TO TAKE ACTION TAB ON NAVIGATION HEADER
• 4 BOXES BELOW MAIN IMAGE WITH IMAGE/DESCRIPTIONS FOR MAKE, SAVE, SPEND, SHARE THAT EACH GO TO THE PAGES FROM THE NAVIGATION HEADER
• EACH PAGE SHOULD BE DEDICATED TO THOSE TOPICS THEN THERE IS AN INTRO ON EACH PAGE THEN THE LINKS TO DIFFERENT BLOGS AROUND EACH TOPIC FOR MAKE, SAVE, SPEND, SHARE
• EACH BLOG SHOULD HAVE COMMENTS SECTION AND SOCIAL MEDIA ICONS
• (GOOD TO USE PINKS/GREYS)
Should not have
• BE SUPER BUSY, CLUTTERED, FEEL LIKE I AM SELLING SOMETHING

```html
<!DOCTYPE html>
<html lang="en">
<head>
<meta charset="utf-8">
<title>Lady Coin Maven</title>
<link href="https://fonts.googleapis.com/css2?family=Lato:wght@300;400;700;900&family=Montserrat:wght@300;400&display=swap" rel="stylesheet">
<style>
:root{
  --pink:#e34197;
  --pink-soft:#e667a6;
  --pink-light:#eea4c8;
  --grey-light:#cbcbcb;
  --grey:#aaaaaa;
  --grey-dark:#959595;
  --ink:#222222;
  --panel:#e6e6e6;
  --hero:#212124;
}
html,body{margin:0;padding:0;overflow:hidden;}
body{font-family:'Lato',sans-serif;color:var(--ink);background:#fff;}
.canvas{position:relative;width:1200px;height:3085px;overflow:hidden;background:#fff;}
.abs{position:absolute;}
/* header */
.call{left:116px;top:20px;display:flex;align-items:center;gap:12px;}
.call-icon{width:36px;height:36px;border-radius:50%;background:var(--pink);display:flex;align-items:center;justify-content:center;box-shadow:0 6px 8px -4px rgba(227,65,151,.35);}
.call small{display:block;font-size:13px;color:#333;line-height:16px;}
.call strong{display:block;font-size:16px;font-weight:400;color:var(--pink);line-height:20px;}
.social-top{left:740px;top:32px;display:flex;gap:22px;}
.social-top i{width:20px;height:20px;border-radius:4px;border:2px solid var(--pink);box-sizing:border-box;}
.take-action{left:943px;top:21px;width:141px;height:42px;background:var(--pink);color:#fff;font-weight:700;font-size:16px;display:flex;align-items:center;justify-content:center;}
.rule{height:2px;background:var(--pink);}
.nav{font-size:16px;color:#222;}
.nav span{position:absolute;white-space:nowrap;}
.nav .dot::after{content:"";display:inline-block;width:9px;height:9px;border-radius:50%;background:var(--pink);margin-left:9px;vertical-align:1px;}
.brand-box{left:499px;top:66px;width:186px;height:98px;background:#f1f1f1;border:1px solid #d8d8d8;box-shadow:0 2px 4px rgba(0,0,0,.18);display:flex;flex-direction:column;align-items:center;justify-content:center;gap:6px;z-index:2;}
.brand-mark{width:26px;height:26px;border-radius:50%;background:var(--pink-light);}
.brand-name{font-size:18px;color:var(--pink);}
/* hero */
.hero-title{left:617px;top:296px;font-size:42px;font-weight:700;color:#fff;line-height:57px;margin:0;}
.btn-outline{left:623px;top:434px;width:160px;height:58px;border:2px solid #fff;color:#fff;font-weight:700;font-size:18px;display:flex;align-items:center;justify-content:center;box-sizing:border-box;}
.mouse{left:588px;top:572px;width:34px;height:50px;border:2px solid #fff;border-radius:14px;box-sizing:border-box;}
.mouse::after{content:"";position:absolute;left:13px;top:9px;width:4px;height:12px;background:#fff;border-radius:2px;}
/* cards */
.card{width:223px;height:251px;top:731px;border:1px solid var(--grey-light);box-shadow:0 2px 4px rgba(0,0,0,.14);background:#fff;text-align:center;box-sizing:border-box;}
.card-img{position:relative;height:125px;}
.card-badge{position:absolute;right:0;bottom:0;width:42px;height:40px;background:var(--pink);display:flex;align-items:center;justify-content:center;}
.card h3{margin:32px 0 6px;font-size:17px;font-weight:900;}
.card p{margin:0;font-size:12.5px;line-height:21px;color:#333;}
/* welcome */
.welcome-bg{left:0;top:1081px;width:453px;height:489px;background:var(--panel);}
.frame{background:#fff;padding:6px;box-shadow:0 1px 4px rgba(0,0,0,.18);box-sizing:border-box;}
.frame div{width:100%;height:100%;}
.welcome-title{left:540px;top:1116px;font-size:31px;font-weight:400;color:#444;margin:0;letter-spacing:-.2px;}
.welcome-text{left:547px;top:1168px;width:514px;font-size:14.6px;line-height:27.5px;color:#444;text-align:justify;margin:0;}
.btn-dark{left:547px;top:1366px;width:148px;height:56px;background:#000;color:#fff;font-size:20px;display:flex;align-items:center;justify-content:center;gap:12px;}
/* mission */
.mission{left:0;top:1570px;width:1200px;height:500px;background:#060606;}
.mission-photo{left:600px;top:1570px;width:600px;height:500px;
  background:
   radial-gradient(ellipse 150px 120px at 50% 68%,#f2c4cf 0%,#e9a9b8 55%,rgba(233,169,184,0) 100%),
   radial-gradient(ellipse 190px 230px at 88% 30%,#6d8db2 0%,#4d6a8e 50%,rgba(77,106,142,0) 100%),
   linear-gradient(180deg,rgba(0,0,0,0) 70%,#e9e9ea 100%),
   linear-gradient(90deg,#060606 0%,#2a2c30 22%,#c7cbd2 55%,#e1e4e8 100%);}
.mission-title{left:114px;top:1622px;font-size:40px;font-weight:700;color:#fff;margin:0;}
.mission-text{left:114px;top:1695px;width:645px;font-size:14.8px;line-height:28.4px;color:#fff;margin:0;}
.btn-light{left:111px;top:1889px;width:154px;height:50px;background:#f2f2f2;color:#111;font-size:20px;display:flex;align-items:center;justify-content:center;gap:12px;border-radius:2px;}
/* blogs */
.blogs-title{left:0;top:2138px;width:1232px;text-align:center;font-size:41px;font-weight:700;margin:0;}
.post{top:2259px;width:474px;height:281px;border:1px solid var(--grey-light);box-shadow:0 2px 5px rgba(0,0,0,.14);display:flex;background:#fff;box-sizing:border-box;}
.post-img{width:171px;height:100%;flex:none;}
.post-body{position:relative;padding:22px 24px 0 34px;flex:1;}
.post-body h4{margin:0;font-size:20px;font-weight:700;letter-spacing:-.6px;color:#222;}
.post-body time{display:block;font-size:11.5px;margin-top:9px;color:#333;}
.post-rule{width:60px;height:1px;background:var(--pink);margin:24px 0 18px;}
.post-body p{margin:0;font-family:'Montserrat',sans-serif;font-weight:300;font-size:13px;line-height:24px;color:#666;width:250px;}
.post-meta{display:flex;align-items:center;gap:8px;margin-top:22px;font-size:10px;color:#666;}
.post-user{position:absolute;right:22px;top:208px;width:28px;height:28px;background:var(--pink);display:flex;align-items:center;justify-content:center;}
.post-share{display:flex;gap:14px;margin-top:16px;}
.post-share i{width:10px;height:10px;border-radius:2px;background:#555;}
/* footer */
.footer{left:0;top:2683px;width:1200px;height:359px;
  background:
   radial-gradient(ellipse 140px 220px at 3% 80%,rgba(160,40,90,.45),rgba(160,40,90,0)),
   radial-gradient(ellipse 140px 220px at 97% 80%,rgba(160,40,90,.45),rgba(160,40,90,0)),
   linear-gradient(180deg,#e64a9c,#e2489a);}
.footer-mark{left:584px;top:2728px;width:48px;height:48px;border-radius:50%;border:3px solid #fff;box-sizing:border-box;}
.footer-name{left:0;top:2780px;width:1216px;text-align:center;font-size:30px;color:#fff;}
.footer-links{left:323px;top:2862px;font-size:19px;color:#fff;white-space:nowrap;}
.footer-links span{margin-right:17px;}
.footer-contact{left:116px;top:2910px;display:flex;align-items:center;gap:14px;font-size:19px;color:#fff;white-space:nowrap;}
.footer-social{left:532px;top:2978px;display:flex;gap:22px;}
.footer-social i{width:20px;height:20px;border-radius:4px;border:2px solid #fff;box-sizing:border-box;}
.legal{left:116px;top:3057px;font-size:12.5px;color:#222;}
.code{left:1127px;top:3059px;font-size:11px;color:#333;}
</style>
</head>
<body>
<div class="canvas">

  <!-- header -->
  <div class="abs call">
    <div class="call-icon">
      <svg width="18" height="18" viewBox="0 0 24 24"><path fill="#fff" d="M6.6 10.8a15 15 0 006.6 6.6l2.2-2.2c.3-.3.7-.4 1-.2 1.1.4 2.3.6 3.6.6.6 0 1 .4 1 1V20c0 .6-.4 1-1 1A17 17 0 013 4c0-.6.4-1 1-1h3.5c.6 0 1 .4 1 1 0 1.3.2 2.5.6 3.6.1.3 0 .7-.2 1z"/></svg>
    </div>
    <div><small>Call Us Today</small><strong>555-010-2040</strong></div>
  </div>
  <div class="abs social-top"><i></i><i></i><i></i><i></i></div>
  <div class="abs take-action">TAKE ACTION</div>

  <div class="abs rule" style="left:102px;top:85px;width:980px;"></div>
  <div class="abs rule" style="left:102px;top:148px;width:980px;"></div>
  <nav class="abs nav" style="left:0;top:110px;">
    <span class="dot" style="left:104px;">MAKE</span>
    <span class="dot" style="left:208px;">SAVE</span>
    <span class="dot" style="left:299px;">SPEND</span>
    <span class="dot" style="left:415px;">SHARE</span>
  </nav>
  <nav class="abs nav" style="left:0;top:107px;">
    <span class="dot" style="left:697px;">MISSION</span>
    <span class="dot" style="left:805px;">GET STARTED</span>
    <span class="dot" style="left:948px;">CONTACT LCM</span>
  </nav>
  <div class="abs brand-box"><i class="brand-mark"></i><span class="brand-name">Lady Coin Maven</span></div>

  <!-- hero -->
  <svg class="abs" style="left:0;top:156px;" width="1200" height="550" viewBox="0 0 1200 550" role="img" aria-label="Hand swinging a hammer into a piggy bank as gold coins and shards burst out">
    <defs>
      <linearGradient id="heroBase" x1="0" x2="1" y1="0" y2="0">
        <stop offset="0" stop-color="#5a6272"/>
        <stop offset=".35" stop-color="#3a3e47"/>
        <stop offset=".55" stop-color="#242528"/>
        <stop offset="1" stop-color="#1f1f22"/>
      </linearGradient>
      <radialGradient id="coins" cx=".22" cy=".62" r=".32">
        <stop offset="0" stop-color="#e6cf7e"/>
        <stop offset=".45" stop-color="#b99a4c" stop-opacity=".85"/>
        <stop offset="1" stop-color="#8a8a86" stop-opacity="0"/>
      </radialGradient>
      <radialGradient id="glow" cx=".12" cy=".2" r=".35">
        <stop offset="0" stop-color="#8a93a4" stop-opacity=".7"/>
        <stop offset="1" stop-color="#8a93a4" stop-opacity="0"/>
      </radialGradient>
    </defs>
    <path d="M0 0H1200V474Q900 479 600 504Q300 484 0 459Z" fill="url(#heroBase)"/>
    <path d="M0 0H1200V474Q900 479 600 504Q300 484 0 459Z" fill="url(#glow)"/>
    <path d="M0 0H1200V474Q900 479 600 504Q300 484 0 459Z" fill="url(#coins)"/>
    <path d="M0 459Q300 484 600 504Q900 479 1200 474V494Q900 504 600 540Q300 520 0 500Z" fill="#e8489a"/>
    <path d="M585 545Q900 512 1200 498" stroke="#e8489a" stroke-width="2" fill="none"/>
  </svg>
  <h1 class="abs hero-title">Rethink the way you think<br>about growing</h1>
  <div class="abs btn-outline">GET STARTED</div>
  <div class="abs mouse"></div>

  <!-- topic cards -->
  <article class="abs card" style="left:119px;">
    <div class="card-img" role="img" aria-label="Man at a laptop holding banknotes" style="background:radial-gradient(ellipse 60px 70px at 72% 45%,#8a6e5e,rgba(138,110,94,0)),radial-gradient(ellipse 50px 30px at 38% 72%,#3d4148,rgba(61,65,72,0)),linear-gradient(180deg,#eef0f0 0%,#d9dcdc 60%,#b9bdbb 100%);">
      <div class="card-badge"><svg width="24" height="18" viewBox="0 0 24 18"><rect x="1" y="3" width="18" height="12" fill="none" stroke="#fff" stroke-width="1.6"/><circle cx="10" cy="9" r="3" fill="none" stroke="#fff" stroke-width="1.6"/><path d="M5 1H23V13" fill="none" stroke="#fff" stroke-width="1.6"/></svg></div>
    </div>
    <h3>MAKE</h3><p>Lorem ipsum dolor sit amet,<br>consectetur adipiscing elit, sed</p>
  </article>
  <article class="abs card" style="left:365px;">
    <div class="card-img" role="img" aria-label="Hand dropping a coin into a piggy bank beside a calculator" style="background:radial-gradient(ellipse 45px 35px at 60% 72%,#f4dbe0,rgba(244,219,224,0)),radial-gradient(ellipse 70px 35px at 25% 85%,#9a9ea4,rgba(154,158,164,0)),linear-gradient(180deg,#aeb3ba 0%,#dcdee0 45%,#f2f2f2 100%);">
      <div class="card-badge"><svg width="22" height="20" viewBox="0 0 22 20"><ellipse cx="11" cy="5" rx="8" ry="3" fill="none" stroke="#fff" stroke-width="1.6"/><path d="M3 5V10C3 12 19 12 19 10V5M3 10V15C3 17 19 17 19 15V10" fill="none" stroke="#fff" stroke-width="1.6"/></svg></div>
    </div>
    <h3>SAVE</h3><p>Lorem ipsum dolor sit amet,<br>consectetur adipiscing elit, sed</p>
  </article>
  <article class="abs card" style="left:612px;">
    <div class="card-img" role="img" aria-label="Banknotes being taken from a leather wallet" style="background:radial-gradient(ellipse 70px 35px at 40% 82%,#7a4630,rgba(122,70,48,0)),radial-gradient(ellipse 50px 40px at 62% 30%,#a9b59a,rgba(169,181,154,0)),linear-gradient(180deg,#2b2626 0%,#4a3a33 55%,#8c7b6c 100%);">
      <div class="card-badge"><svg width="22" height="18" viewBox="0 0 22 18"><rect x="1" y="3" width="20" height="14" rx="2" fill="none" stroke="#fff" stroke-width="1.6"/><rect x="13" y="8" width="8" height="4" fill="none" stroke="#fff" stroke-width="1.6"/><path d="M3 3L15 0V3" fill="none" stroke="#fff" stroke-width="1.6"/></svg></div>
    </div>
    <h3>SPEND</h3><p>Lorem ipsum dolor sit amet,<br>consectetur adipiscing elit, sed</p>
  </article>
  <article class="abs card" style="left:859px;">
    <div class="card-img" role="img" aria-label="Many hands holding coins together" style="background:radial-gradient(ellipse 55px 45px at 50% 55%,#c9cdd2,rgba(201,205,210,0)),radial-gradient(ellipse 100px 60px at 50% 50%,#a98a7a,rgba(169,138,122,0)),linear-gradient(135deg,#3f5a78,#6f8aa5 50%,#34435a);">
      <div class="card-badge"><svg width="20" height="18" viewBox="0 0 20 18"><path d="M10 17C4 12 1 9 1 5.5A4.5 4.5 0 0110 3.5A4.5 4.5 0 0119 5.5C19 9 16 12 10 17Z" fill="none" stroke="#fff" stroke-width="1.6"/></svg></div>
    </div>
    <h3>SHARE</h3><p>Lorem ipsum dolor sit amet,<br>consectetur adipiscing elit, sed</p>
  </article>

  <!-- welcome -->
  <div class="abs welcome-bg"></div>
  <div class="abs frame" style="left:213px;top:1139px;width:276px;height:184px;"><div role="img" aria-label="Woman putting a coin into a piggy bank" style="background:radial-gradient(ellipse 60px 40px at 75% 80%,#f0c5c8,rgba(240,197,200,0)),radial-gradient(ellipse 80px 70px at 40% 40%,#c99680,rgba(201,150,128,0)),linear-gradient(135deg,#5e3f33,#9b6f5c 55%,#d6b2a6);"></div></div>
  <div class="abs frame" style="left:61px;top:1217px;width:262px;height:185px;"><div role="img" aria-label="Cupped hands holding coins" style="background:radial-gradient(ellipse 70px 50px at 55% 45%,#d9c0b4,rgba(217,192,180,0)),radial-gradient(ellipse 40px 30px at 75% 25%,#b04a58,rgba(176,74,88,0)),linear-gradient(135deg,#a7adb6,#7e838c 55%,#4e525a);"></div></div>
  <div class="abs frame" style="left:211px;top:1285px;width:240px;height:181px;"><div role="img" aria-label="Mother and daughter with a pink piggy bank" style="background:radial-gradient(ellipse 55px 35px at 55% 82%,#f5c0d0,rgba(245,192,208,0)),radial-gradient(ellipse 50px 60px at 30% 40%,#e0b79c,rgba(224,183,156,0)),radial-gradient(ellipse 50px 60px at 72% 42%,#edc8ae,rgba(237,200,174,0)),linear-gradient(180deg,#d8dccb 0%,#c9c4b0 60%,#3f9c86 100%);"></div></div>
  <h2 class="abs welcome-title">Welcome to Lady Coin Maven (LCM)!</h2>
  <p class="abs welcome-text">Lorem ipsum dolor sit amet, consectetur adipiscing elit, sed do eiusmod tempor incididunt ut labore et dolore magna aliqua. Quis ipsum suspendisse ultrices gravida. Risus commodo viverra maecenas accumsan lacus vel facilisis. Lorem ipsum dolor sit amet, consectetur adipiscing elit, sed do eiusmod tempor incididunt ut labore et dolore magna aliqua. Quis ipsum suspendisse ultrices gravida. Risus commodo viverra maecenas accumsan lacus vel facilisis.</p>
  <div class="abs btn-dark">Read More <svg width="22" height="16" viewBox="0 0 22 16"><path d="M0 0L10 8L0 16ZM11 0L21 8L11 16Z" fill="#fff"/></svg></div>

  <!-- mission -->
  <section class="abs mission"></section>
  <div class="abs mission-photo" role="img" aria-label="Woman in a denim shirt putting a coin into a pink spotted piggy bank"></div>
  <h2 class="abs mission-title">Our Mission</h2>
  <p class="abs mission-text">Lorem ipsum dolor sit amet, consectetur adipiscing elit, sed do eiusmod tempor incididunt ut labore et dolore magna aliqua. Quis ipsum suspendisse ultrices gravida. Risus commodo viverra maecenas accumsan lacus vel facilisis. Lorem ipsum dolor sit amet, consectetur adipiscing elit, sed do eiusmod tempor incididunt ut labore et dolore magna aliqua. Quis ipsum suspendisse ultrices gravida. Risus commodo viverra maecenas accumsan lacus vel facilisis.</p>
  <div class="abs btn-light">Read More <svg width="22" height="16" viewBox="0 0 22 16"><path d="M0 0L10 8L0 16ZM11 0L21 8L11 16Z" fill="#111"/></svg></div>

  <!-- blogs -->
  <h2 class="abs blogs-title">Blogs &amp; News</h2>
  <article class="abs post" style="left:108px;">
    <div class="post-img" role="img" aria-label="Glass jar filled with coins" style="background:radial-gradient(ellipse 55px 70px at 50% 68%,#c8b9a0,rgba(200,185,160,0)),radial-gradient(ellipse 60px 110px at 50% 55%,#d9d6dc,rgba(217,214,220,0)),linear-gradient(180deg,#9c8bb0 0%,#b4a9bf 50%,#7c6650 100%);"></div>
    <div class="post-body">
      <h4>Lorem ipsum is best</h4><time>on May 28, 2019 9:58 AM</time>
      <div class="post-rule"></div>
      <p>Lorem ipsum dolor sit amet, consectetur adipiscing elit, sed do eiusmod tempor incididunt ut labore</p>
      <div class="post-meta">
        <svg width="12" height="11" viewBox="0 0 12 11"><rect x=".5" y=".5" width="11" height="8" fill="none" stroke="#777"/><path d="M3 8.5V10.5L5 8.5" fill="none" stroke="#777"/></svg><span>24 comments</span>
        <svg style="margin-left:18px" width="14" height="13" viewBox="0 0 14 13"><path d="M1 6H4V12H1ZM4 6L7 1C8 1 8.5 2 8 4H12.5L11 12H4" fill="none" stroke="#777"/></svg><span>500K</span>
      </div>
      <div class="post-share"><i></i><i></i><i></i><i></i><i></i></div>
      <div class="post-user"><svg width="16" height="16" viewBox="0 0 16 16"><circle cx="8" cy="5" r="3.2" fill="none" stroke="#fff" stroke-width="1.5"/><path d="M2 15C2 11 5 9.5 8 9.5S14 11 14 15Z" fill="none" stroke="#fff" stroke-width="1.5"/></svg></div>
    </div>
  </article>
  <article class="abs post" style="left:612px;">
    <div class="post-img" role="img" aria-label="Fingers placing a coin on a stack of coins in warm light" style="background:radial-gradient(ellipse 40px 60px at 35% 70%,#8e7a5a,rgba(142,122,90,0)),radial-gradient(ellipse 60px 50px at 60% 20%,#b48a6a,rgba(180,138,106,0)),linear-gradient(180deg,#4f4a1e 0%,#8a7a36 45%,#d6aa4c 80%,#f2cf72 100%);"></div>
    <div class="post-body">
      <h4>Lorem ipsum is best</h4><time>on May 28, 2019 9:58 AM</time>
      <div class="post-rule"></div>
      <p>Lorem ipsum dolor sit amet, consectetur adipiscing elit, sed do eiusmod tempor incididunt ut labore</p>
      <div class="post-meta">
        <svg width="12" height="11" viewBox="0 0 12 11"><rect x=".5" y=".5" width="11" height="8" fill="none" stroke="#777"/><path d="M3 8.5V10.5L5 8.5" fill="none" stroke="#777"/></svg><span>24 comments</span>
        <svg style="margin-left:18px" width="14" height="13" viewBox="0 0 14 13"><path d="M1 6H4V12H1ZM4 6L7 1C8 1 8.5 2 8 4H12.5L11 12H4" fill="none" stroke="#777"/></svg><span>500K</span>
      </div>
      <div class="post-share"><i></i><i></i><i></i><i></i><i></i></div>
      <div class="post-user"><svg width="16" height="16" viewBox="0 0 16 16"><circle cx="8" cy="5" r="3.2" fill="none" stroke="#fff" stroke-width="1.5"/><path d="M2 15C2 11 5 9.5 8 9.5S14 11 14 15Z" fill="none" stroke="#fff" stroke-width="1.5"/></svg></div>
    </div>
  </article>

  <!-- footer -->
  <footer class="abs footer"></footer>
  <div class="abs footer-mark"></div>
  <div class="abs footer-name">Lady Coin Maven</div>
  <div class="abs footer-links"><span>Make</span><span>Save</span><span>Spend</span><span>Share</span><span style="margin-right:25px">Mission</span><span style="margin-right:25px">Get started</span><span>Contact Me</span></div>
  <div class="abs footer-contact">
    <svg width="26" height="26" viewBox="0 0 24 24"><path fill="#fff" d="M6.6 10.8a15 15 0 006.6 6.6l2.2-2.2c.3-.3.7-.4 1-.2 1.1.4 2.3.6 3.6.6.6 0 1 .4 1 1V20c0 .6-.4 1-1 1A17 17 0 013 4c0-.6.4-1 1-1h3.5c.6 0 1 .4 1 1 0 1.3.2 2.5.6 3.6.1.3 0 .7-.2 1z"/></svg>
    <span>(555) 010 2040</span>
    <svg width="22" height="28" viewBox="0 0 24 30" style="margin-left:4px"><path fill="#fff" d="M12 0a10 10 0 00-10 10c0 8 10 20 10 20s10-12 10-20A10 10 0 0012 0zm0 14a4 4 0 110-8 4 4 0 010 8z"/></svg>
    <span>48 Maple Row, dolor sit amet, Consectetur adiping,</span>
    <svg width="32" height="22" viewBox="0 0 32 22" style="margin-left:14px"><rect x="1" y="1" width="30" height="20" fill="none" stroke="#fff" stroke-width="2"/><path d="M1 1L16 13L31 1" fill="none" stroke="#fff" stroke-width="2"/></svg>
    <span>hello@ladycoinmaven.example</span>
  </div>
  <div class="abs footer-social"><i></i><i></i><i></i><i></i></div>
  <div class="abs legal">© 2019 All Rights Reserved | Privacy Policy | Terms and Conditions</div>
  <div class="abs code">C36</div>

</div>
</body>
</html>
```